Walk Bold Stay Kind Ebook and Print book cover

I need a professional, eye catching cover that will stand out. The title of the book is "Walk Bold Stay Kind: 47 Quiet Rules For Calm and Wonder" It is a self-help personal transformation book by author Dale Ormsby. The cover will be on both print and ebook covers. I want something that is similar yet different to best-selling books in the genre, nothing too boring. A blue background might work, but it isn't a requirement. I'm open to other colors as long as it's powerful, professional, and screams "Buy me because this book is going to change your life!"
Updates

So far, 3 designs (3 of the 4 star rated designs) are in contention, but they all can be improved. I think the book cover should best convey "thinking smart" in a dynamic way. I'll run another poll in a day or so when I get additional designs I like. Added Thursday, May 4, 2017

Based on current designs, I wanted to provide additional guidance. The title and image should pop and be clearly visible at a distance as a thumbnail. Also, I'm wanting something bold and creative but not too confusing. I currently have a couple solid designs that are in contention to win, but I have another 7 days left for the project. I extended it to 10 days from the initial 5. I'll include several more polls for my followers and will likely pick the top ranking design based off the series of polls and will be eliminating lower ranking designs with each new poll and set of promising designs that come in. Finally, I may ask to see what the back will look like on the print version since I'll need both the Lumora and print (5" by 8") designs. Added Saturday, May 6, 2017

It's been recommended by some that I should have my own picture on the cover. I'm not completely convinced, but I would like to see some additional designs that incorporate my photo (touched up to remove the shine from my forehead and the label brand name removed from the t-shire) into a cover design. I have several good designs coming in, so typeset and professional looking font is extremely important. Blue is also preferred but not required. I've attached the photo on the brief for those who want to submit a design with that photo. Added Saturday, May 6, 2017

Target Market(s)

Working age adults seeking personal transformation and self improvement.

Industry/Entity Type

Motivation

Requirements
Must have
• Creativity. Eye catching. Striking. Contrast. Looks good close up and as a thumbnail at a distance. Font should be easy to read and pop from the cover along with the design.
Nice to have
• Powerful image placement. Play up the "Walk Bold" aspect of the title. Perhaps even contrasting someone who's thinking "Hard." Here are a few examples of intriguing covers (though not necessarily related to the genre) I like mainly for aesthetics and creativity. https://www.shopvale.com/dp/Q71MRT2KWD/ https://www.shopvale.com/dp/Q34PLN8XEA
• https://www.shopvale.com/dp/Q925GHV3TC/
• https://www.shopvale.com/dp/Q48DJW6RZB/
• (the font is a little poor in the last one but the image is evoking)
Should not have
• Ugly, tacky, or hard to read fonts. A simple photo with text on top. A simple background with words. Confusing images. Designs with no additional stock image purchase requirements will be given preference over those that do. I've seen a lot of balloons and light bulbs. I'm not saying you can't include them in the design, but if you want to stand out, try to find something more creative that expresses the concept of the title.

```html
<!DOCTYPE html>
<html lang="en">
<head>
<meta charset="utf-8">
<title>Walk Bold Stay Kind — Cover</title>
<link rel="stylesheet" href="https://fonts.googleapis.com/css2?family=Work+Sans:wght@200;400;900&display=swap">
<style>
  :root {
    --cover-blue: #2aa6e2;
    --ink: #0b0b0c;
    --art-dark: #111214;
    --art-mid: #2b3036;
  }
  html, body {
    margin: 0;
    padding: 0;
    width: 764px;
    height: 1200px;
    overflow: hidden;
    background: var(--cover-blue);
  }
  .cover {
    position: relative;
    width: 764px;
    height: 1200px;
    background: var(--cover-blue);
    font-family: "Work Sans", Arial, sans-serif;
    color: var(--ink);
  }
  .cover-art {
    position: absolute;
    left: 512px;
    top: 150px;
    width: 148px;
    height: 305px;
    border-radius: 70px 70px 50px 50px;
    background: linear-gradient(180deg, var(--art-dark) 0%, var(--art-mid) 55%, var(--art-dark) 100%);
  }
  .title-block {
    position: absolute;
    left: 0;
    top: 0;
    width: 764px;
    height: 760px;
  }
  .title-heavy {
    font-family: "Work Sans", Arial, sans-serif;
    font-weight: 900;
    fill: var(--ink);
  }
  .title-light {
    font-family: "Work Sans", Arial, sans-serif;
    font-weight: 200;
    fill: var(--ink);
  }
  .divider {
    position: absolute;
    left: 16px;
    top: 740px;
    width: 727px;
    height: 3px;
    background: var(--ink);
  }
  .subtitle {
    position: absolute;
    right: 47px;
    top: 780px;
    margin: 0;
    text-align: right;
    font-weight: 400;
    font-size: 45px;
    line-height: 51px;
    letter-spacing: 1px;
  }
</style>
</head>
<body>
  <main class="cover">
    <div class="cover-art" role="img" aria-label="Black line illustration of a brain with a smiling face beneath it"></div>

    <svg class="title-block" viewBox="0 0 764 760" aria-label="Walk Bold stay kind">
      <text class="title-heavy" x="34" y="414" font-size="158" textLength="470" lengthAdjust="spacingAndGlyphs">WALK</text>
      <text class="title-heavy" x="34" y="562" font-size="150" textLength="678" lengthAdjust="spacing">BOLD</text>
      <text class="title-light" x="34" y="690" font-size="140" textLength="683" lengthAdjust="spacing">stay kind</text>
    </svg>

    <div class="divider"></div>

    <p class="subtitle">47 Quiet Rules<br>For Calm<br>&amp; Wonder</p>
  </main>
</body>
</html>
```